High-end residential home builder needs a business card design

We need a new business card design for a small residential construction company based in Boise, Idaho. We specialize in building custom high-end homes and remodels, with a focus on great design and craftsmanship.

We would like to use our current logo, but open to new color suggestions.
Just looking for a clean, sharp, modern design that looks high-end.

Target Market(s)

Upscale clientele

Industry/Entity Type

Contractor

Contact Information for Business Card

Company: Stonehaven Custom Builders
Name: Colin Marsh
Phone number: 208 637 4120
Email: ColinMarshSCB@quillpost.net
Website: Stonehavencustombuilders.com

Font styles to use
Serif
Sans Serif

Requirements
Must have
• Company Logo
Company name
My name
My phone number
My email
Company website
Nice to have
• I have attached a few photos of cards that I really like.

```html
<!DOCTYPE html>
<html lang="en">
<head>
<meta charset="utf-8">
<title>Stonehaven Custom Builders – Business Card</title>
<link href="https://fonts.googleapis.com/css2?family=Montserrat:wght@400;500;700&family=Roboto+Slab:wght@400&display=swap" rel="stylesheet">
<style>
  :root {
    --backdrop: #c4c4c4;
    --card-grey: #7a7a76;
    --card-white: #ffffff;
    --ink: #2f1c10;
    --accent: #e08a1e;
    --light: #ffffff;
  }
  * { box-sizing: border-box; margin: 0; padding: 0; }
  html, body {
    width: 1200px; height: 900px; overflow: hidden;
    background: var(--backdrop);
  }
  .canvas {
    width: 1200px; height: 900px;
    display: flex; flex-direction: column; align-items: center; justify-content: center;
    gap: 30px;
  }
  .card {
    width: 620px; height: 340px;
    border-radius: 26px;
    position: relative;
    overflow: hidden;
    box-shadow: 0 10px 22px rgba(0,0,0,0.25);
  }

  /* Shared brand block */
  .brand {
    display: flex; align-items: center; gap: 26px;
  }
  .brand__mark {
    width: 74px; height: 74px;
    border: 3px solid currentColor;
    flex: none;
  }
  .brand__name {
    font-family: "Montserrat", sans-serif;
    font-weight: 500;
    text-transform: uppercase;
    line-height: 1.35;
  }
  .brand__line1 { display: block; font-size: 30px; letter-spacing: 0.36em; }
  .brand__line2 { display: block; font-size: 17px; letter-spacing: 0.42em; padding-left: 36px; }

  /* Back side */
  .card--back {
    background: var(--card-grey);
    display: flex; flex-direction: column; align-items: center; justify-content: center;
  }
  .card--back .brand { color: var(--light); }
  .tagline {
    margin-top: 54px;
    font-family: "Montserrat", sans-serif;
    font-weight: 500;
    font-size: 17px;
    letter-spacing: 0.06em;
    color: var(--accent);
    text-transform: uppercase;
  }

  /* Front side */
  .card--front {
    background: var(--card-white);
    padding: 50px 56px;
  }
  .card--front .brand { color: var(--ink); }
  .card--front .brand__mark { width: 66px; height: 66px; }
  .card--front .brand__line1 { font-size: 27px; }
  .card--front .brand__line2 { font-size: 15px; }
  .person {
    margin-top: 46px;
    font-family: "Montserrat", sans-serif;
    font-weight: 700;
    font-size: 27px;
    color: var(--ink);
    text-transform: uppercase;
    letter-spacing: 0.01em;
  }
  .contact {
    list-style: none;
    margin-top: 14px;
    font-family: "Roboto Slab", serif;
    font-size: 18px;
    color: var(--ink);
    line-height: 1.5;
  }
  .contact__item { display: flex; align-items: center; gap: 12px; }
  .contact__icon { width: 18px; height: 18px; flex: none; fill: var(--ink); }
  .contact__domain { color: var(--accent); }
</style>
</head>
<body>
<main class="canvas">

  <section class="card card--back" aria-label="Card back">
    <div class="brand">
      <span class="brand__mark" aria-hidden="true"></span>
      <p class="brand__name">
        <span class="brand__line1">Stonehaven</span>
        <span class="brand__line2">Custom Builders</span>
      </p>
    </div>
    <p class="tagline">Crafted with purpose</p>
  </section>

  <section class="card card--front" aria-label="Card front">
    <div class="brand">
      <span class="brand__mark" aria-hidden="true"></span>
      <p class="brand__name">
        <span class="brand__line1">Stonehaven</span>
        <span class="brand__line2">Custom Builders</span>
      </p>
    </div>

    <h1 class="person">Colin Marsh</h1>

    <ul class="contact">
      <li class="contact__item">
        <svg class="contact__icon" viewBox="0 0 24 24" aria-hidden="true"><path d="M6.6 10.8a15.1 15.1 0 0 0 6.6 6.6l2.2-2.2c.3-.3.7-.4 1-.2 1.1.4 2.3.6 3.6.6.6 0 1 .4 1 1V20c0 .6-.4 1-1 1A17 17 0 0 1 3 4c0-.6.4-1 1-1h3.5c.6 0 1 .4 1 1 0 1.3.2 2.5.6 3.6.1.3 0 .7-.2 1z"/></svg>
        <span>208 637 4120</span>
      </li>
      <li class="contact__item">
        <svg class="contact__icon" viewBox="0 0 24 24" aria-hidden="true"><path d="M2 5h20v14H2z M4 7v.4l8 5 8-5V7l-8 5z" fill-rule="evenodd"/></svg>
        <span>ColinMarshSCB@quillpost.net</span>
      </li>
      <li class="contact__item">
        <svg class="contact__icon" viewBox="0 0 24 24" aria-hidden="true"><path d="M12 2a10 10 0 1 0 0 20 10 10 0 0 0 0-20zm6.9 6h-2.9a15.7 15.7 0 0 0-1.4-3.6A8 8 0 0 1 18.9 8zM12 4c.8 1.2 1.5 2.5 1.9 4h-3.8c.4-1.5 1.1-2.8 1.9-4zM4.3 14a8 8 0 0 1 0-4h3.4a16.5 16.5 0 0 0 0 4zm.8 2h2.9c.3 1.3.8 2.5 1.4 3.6A8 8 0 0 1 5.1 16zM8 8H5.1a8 8 0 0 1 4.3-3.6C8.8 5.5 8.3 6.7 8 8zm4 12c-.8-1.2-1.5-2.5-1.9-4h3.8c-.4 1.5-1.1 2.8-1.9 4zm2.3-6H9.7a14.7 14.7 0 0 1 0-4h4.6a14.7 14.7 0 0 1 0 4zm.3 5.6c.6-1.1 1.1-2.3 1.4-3.6h2.9a8 8 0 0 1-4.3 3.6zm1.7-5.6a16.5 16.5 0 0 0 0-4h3.4a8 8 0 0 1 0 4z"/></svg>
        <span>www.<span class="contact__domain">Stonehavencustombuilders</span>.com</span>
      </li>
    </ul>
  </section>

</main>
</body>
</html>
```